Create a PPTX template for our business

We need a Powerpoint and Keynote template design for a new company called "Corvanta" We connect hotel guests to hotel employees through text messaging so guests can ask for what they need during their stay. The name "Corvanta" is derived from the word "Affinity" which is how we want our hotel customer's employees and their guests to feel about each other. The color palette chosen is meant to evoke feelings of "warmth" and "comfort," which is how most people feel when they have a strong affinity to each other. The "-ium" ending of Corvanta is intended to give a technological feel to our business since we use technology to connect people together.

A *.ai file is included which contains our logo.

Hotel

```html
<!DOCTYPE html>
<html lang="en">
<head>
<meta charset="utf-8">
<title>Corvanta – Presentation Title Slide</title>
<link href="https://fonts.googleapis.com/css2?family=Roboto+Condensed:wght@300;400&display=swap" rel="stylesheet">
<style>
  :root {
    --teal: #4fc2bc;
    --paper: #efefef;
    --footer: #d2d2d2;
    --white: #ffffff;
    --ink: #5a5a5a;
  }
  html, body {
    margin: 0;
    padding: 0;
    width: 1200px;
    height: 900px;
    overflow: hidden;
    background: var(--paper);
  }
  .slide {
    position: relative;
    width: 1200px;
    height: 900px;
    font-family: "Roboto Condensed", "Arial Narrow", sans-serif;
  }
  .hero {
    position: absolute;
    left: 0;
    top: 0;
    width: 1200px;
    height: 578px;
    background: var(--teal);
  }
  .hero-text {
    position: absolute;
    right: 48px;
    top: 360px;
    text-align: right;
    color: var(--white);
  }
  .project-title {
    margin: 0;
    font-size: 51px;
    font-weight: 400;
    line-height: 1;
    letter-spacing: -0.2px;
  }
  .project-subtext {
    margin: 24px 0 0;
    font-size: 18px;
    font-weight: 400;
    line-height: 30px;
  }
  .brand-band {
    position: absolute;
    left: 0;
    top: 578px;
    width: 1200px;
    height: 280px;
    background:
      radial-gradient(ellipse 500px 18px at 200px 0, rgba(0,0,0,0.06), transparent 70%),
      var(--paper);
  }
  .brand {
    position: absolute;
    right: 48px;
    top: 130px;
    display: flex;
    align-items: center;
    gap: 22px;
  }
  .brand-dot {
    width: 58px;
    height: 58px;
    border-radius: 50%;
    background: var(--teal);
  }
  .brand-name {
    font-size: 50px;
    font-weight: 300;
    letter-spacing: 1px;
    text-transform: uppercase;
    color: var(--ink);
    line-height: 1;
  }
  .footer-strip {
    position: absolute;
    left: 0;
    top: 858px;
    width: 1200px;
    height: 42px;
    background: var(--footer);
  }
</style>
</head>
<body>
  <main class="slide">
    <section class="hero">
      <div class="hero-text">
        <h1 class="project-title">Project Title Here</h1>
        <p class="project-subtext">Subtext here Subtext here Subtext here<br>Subtext here Subtext here Subtext here</p>
      </div>
    </section>
    <section class="brand-band">
      <div class="brand">
        <span class="brand-dot" aria-hidden="true"></span>
        <span class="brand-name">Corvanta</span>
      </div>
    </section>
    <footer class="footer-strip"></footer>
  </main>
</body>
</html>
```